Personal training poster - 1200X900mm

Poster to promote my new personal training service at my gym. The poster will be printed and put into an aframe to be seen by people walking past my gym. It needs to be simple and eye catching with the text i have put in the must haves. The text and image should be the prominent parts of the design.

Target Market(s)

30-50 year old females

Industry/Entity Type

Fitness

Font styles to use
Sans Serif

Requirements
Must have
• my logo
• exercise graphic
• Must include the following text:
• Are you looking for a personal trainer? Our expert trainers can help you achieve you take your health and fitness back!
• Contact details:
• 1300452968
• info@brightmovegym.com.au
• Located under the Harbourview Club

```html
<!DOCTYPE html>
<html lang="en">
<head>
<meta charset="UTF-8">
<title>Brightmove Gym – Personal Training Poster</title>
<link rel="stylesheet" href="https://fonts.googleapis.com/css2?family=Archivo+Black&family=Poppins:wght@600;700&display=swap">
<style>
  :root {
    --backdrop: #a9a99f;
    --paper: #ffffff;
    --headline-blue: #3a7dc6;
    --band-navy: #2f3f98;
    --band-yellow: #f6ef5c;
    --label-grey: #5a5a5a;
    --ink: #1f1f24;
    --sky: #5bc8f0;
    --gold: #f0c230;
    --royal: #2f3f98;
  }
  * { margin: 0; padding: 0; box-sizing: border-box; }
  html, body {
    width: 1200px; height: 1000px; overflow: hidden;
    background: var(--backdrop);
  }
  .poster {
    position: absolute; left: 265px; top: 25px;
    width: 672px; height: 950px;
    background: var(--paper);
    box-shadow: 0 2px 10px rgba(0,0,0,0.25);
    overflow: hidden;
  }
  .brand {
    position: absolute; left: 0; right: 0; top: 86px;
    display: flex; align-items: center; justify-content: center; gap: 10px;
    font-family: "Archivo Black", sans-serif;
    font-size: 24px; line-height: 28px; letter-spacing: 1px;
    color: var(--royal);
  }
  .brand-dot {
    width: 18px; height: 18px; border-radius: 50%;
    background: var(--sky);
  }
  .exercise-graphic {
    position: absolute; left: 75px; top: 128px;
    width: 522px; height: 375px;
    border-radius: 14px;
    background: linear-gradient(160deg, #bfe9f8 0%, #fbe6a0 50%, #b9c0e6 100%);
  }
  .headline {
    position: absolute; left: 0; right: 0; top: 503px;
    text-align: center;
    font-family: "Archivo Black", sans-serif;
    font-size: 57px; line-height: 62px;
    color: var(--headline-blue);
    white-space: nowrap;
  }
  .promise-band {
    position: absolute; left: 0; right: 0; top: 635px; height: 153px;
    background: var(--band-navy);
    display: flex; align-items: center; justify-content: center;
    text-align: center;
    font-family: "Archivo Black", sans-serif;
    font-size: 35px; line-height: 42px;
    color: var(--band-yellow);
    white-space: nowrap;
  }
  .contact {
    position: absolute; left: 20px; top: 790px;
    font-family: "Poppins", sans-serif; font-weight: 700;
  }
  .contact-label {
    margin-left: 57px;
    font-size: 31px; line-height: 42px;
    color: var(--label-grey);
  }
  .contact-item {
    display: flex; align-items: center; gap: 14px;
    font-size: 29px; line-height: 39px;
    color: var(--ink);
    white-space: nowrap;
  }
  .contact-icon { width: 42px; height: 34px; flex: none; }
</style>
</head>
<body>
  <main class="poster">
    <div class="brand"><span class="brand-dot"></span>BRIGHTMOVE GYM</div>

    <div class="exercise-graphic" role="img" aria-label="Exercise graphic: geometric blue and yellow figure lifting a barbell overhead"></div>

    <h1 class="headline">Are you looking for<br>a personal trainer?</h1>

    <p class="promise-band">Our expert trainers can<br>help you achieve you take<br>your health and fitness back!</p>

    <section class="contact">
      <p class="contact-label">Contact details:</p>
      <p class="contact-item">
        <svg class="contact-icon" viewBox="0 0 42 34" aria-hidden="true">
          <path d="M3 12 Q21 0 39 12 L35 17 L29 14 L29 10 Q21 7 13 10 L13 14 L7 17 Z" fill="var(--royal)"/>
          <path d="M11 15 L31 15 L37 31 L5 31 Z" fill="var(--royal)"/>
          <circle cx="21" cy="23" r="5.5" fill="#fff"/>
        </svg>1300452968</p>
      <p class="contact-item">
        <svg class="contact-icon" viewBox="0 0 42 34" aria-hidden="true">
          <rect x="3" y="6" width="36" height="26" rx="2" fill="var(--headline-blue)"/>
          <rect x="10" y="2" width="22" height="16" fill="var(--gold)"/>
          <path d="M3 6 L21 21 L39 6" stroke="#fff" stroke-width="2" fill="none"/>
        </svg>info@brightmovegym.com.au</p>
      <p class="contact-item">
        <svg class="contact-icon" viewBox="0 0 42 34" aria-hidden="true">
          <path d="M21 33 L12 17 A10 10 0 1 1 30 17 Z" fill="var(--sky)"/>
          <circle cx="21" cy="12" r="4.5" fill="var(--gold)"/>
        </svg>Located under the Harbourview Club</p>
    </section>
  </main>
</body>
</html>
```